Design some Business Cards for Vortelix7

i need a company card, something modern related with web solution.

logo area (i provide the .psd) logo can be melted with background i dont really care.
need contact area:
Name
tittle

web site
email
and phone.

color range: i like dark color modern but dark.

```html
<!DOCTYPE html>
<html lang="en">
<head>
<meta charset="utf-8">
<title>Vortelix7 Business Card</title>
<link rel="stylesheet" href="https://fonts.googleapis.com/css2?family=Orbitron:wght@400;500&display=swap">
<style>
  :root {
    --page: #ffffff;
    --card: #0b0d0e;
    --card-edge: #9a9d9f;
    --card-rim: #2a2d2f;
    --mark-box: #3b3c3d;
    --accent: #f0502a;
    --ink: #ffffff;
    --mesh-light: rgba(200, 204, 208, 0.32);
    --mesh-dark: rgba(60, 64, 68, 0.10);
  }
  * { margin: 0; padding: 0; box-sizing: border-box; }
  html, body {
    width: 1017px;
    height: 1200px;
    overflow: hidden;
    background: var(--page);
  }
  .sheet {
    position: relative;
    width: 1017px;
    height: 1200px;
    font-family: "Orbitron", sans-serif;
  }
  .card {
    position: absolute;
    left: 102px;
    width: 829px;
    background: var(--card);
    border: 3px solid var(--card-edge);
    box-shadow: inset 0 0 0 6px var(--card-rim), 8px 18px 26px rgba(0, 0, 0, 0.55);
    overflow: hidden;
  }
  .card--front { top: 105px; height: 448px; }
  .card--back { top: 653px; height: 451px; }

  .mesh { position: absolute; inset: 0; width: 100%; height: 100%; }

  .front-mark {
    position: absolute;
    left: 13px;
    top: 126px;
    width: 204px;
    height: 187px;
    background: var(--mark-box);
    box-shadow: 0 0 40px 14px rgba(120, 124, 128, 0.45);
  }
  .front-name {
    position: absolute;
    left: 222px;
    top: 150px;
    font-size: 98px;
    font-weight: 400;
    line-height: 1;
    color: var(--accent);
    letter-spacing: 1px;
  }

  .back-mark {
    position: absolute;
    left: 54px;
    top: 83px;
    width: 290px;
    height: 269px;
    background: var(--mark-box);
    display: flex;
    align-items: center;
    justify-content: center;
  }
  .back-mark__name {
    font-size: 34px;
    font-weight: 400;
    color: var(--accent);
  }
  .contact {
    position: absolute;
    left: 367px;
    top: 30px;
    color: var(--ink);
    font-weight: 400;
    line-height: 1;
  }
  .contact__name { font-size: 46px; }
  .contact__title { font-size: 40px; margin-top: 18px; }
  .contact__links { margin-top: 122px; font-size: 38px; }
  .contact__links li { list-style: none; margin-bottom: 2px; }
</style>
</head>
<body>
<main class="sheet">

  <section class="card card--front" aria-label="Card front">
    <svg class="mesh" viewBox="0 0 829 448" preserveAspectRatio="none" role="img" aria-label="Flowing wireframe mesh background">
      <defs>
        <radialGradient id="frontGlow" cx="0.62" cy="0.45" r="0.6">
          <stop offset="0" stop-color="var(--mesh-light)"/>
          <stop offset="1" stop-color="var(--mesh-dark)"/>
        </radialGradient>
      </defs>
      <path d="M220 0 H829 V448 H300 C340 360 250 260 240 170 C230 90 260 40 220 0 Z" fill="url(#frontGlow)"/>
    </svg>
    <div class="front-mark"></div>
    <h1 class="front-name">Vortelix7</h1>
  </section>

  <section class="card card--back" aria-label="Card back">
    <svg class="mesh" viewBox="0 0 829 451" preserveAspectRatio="none" role="img" aria-label="Curved wireframe mesh background">
      <defs>
        <linearGradient id="backGlow" x1="0" y1="0" x2="1" y2="0">
          <stop offset="0" stop-color="rgba(210,214,218,0.38)"/>
          <stop offset="1" stop-color="rgba(90,94,98,0.14)"/>
        </linearGradient>
      </defs>
      <path d="M380 0 H829 V451 H420 C560 420 560 60 380 0 Z" fill="url(#backGlow)"/>
    </svg>
    <div class="back-mark">
      <span class="back-mark__name">Vortelix7</span>
    </div>
    <div class="contact">
      <p class="contact__name">Name:</p>
      <p class="contact__title">Title:</p>
      <ul class="contact__links">
        <li>Web Site:</li>
        <li>Email:</li>
        <li>Phone:</li>
      </ul>
    </div>
  </section>

</main>
</body>
</html>
```